Window company needs new banner

Window company that has 3 focuses needs a new banner ad.

We sell window hardware
We make new sashes and windows
We restore old windows

http://www.tlsashandrenewal.com

I would like to create a new banner ad for our home page. The ad would try to capture the 3 sections listed above. I would also say they are listed in importance. Our main focus is hardware for this ad.

our best pictures are on our website.

Our suppliers websites
http://www.brindle.co.uk
http://www.kelphardware.co.uk
https://www.pellowgoods.com

Target Market(s)

Historical buildings
Restoration contractors
window restorers
DIY home owners
custom window and door fabricators- Trades people

Industry/Entity Type

Home And Garden

Font styles to use
Serif

Requirements
Must have
• Show the high level of quality of our hardware and other services

```html
<!DOCTYPE html>
<html lang="en">
<head>
<meta charset="utf-8">
<title>Window Hardware, Restoration and New Sashes – Banners</title>
<link rel="stylesheet" href="https://fonts.googleapis.com/css2?family=Arimo:wght@400;700&display=swap">
<style>
  :root {
    --page: #ffffff;
    --frame: #333333;
    --caption: #111111;
    --swoosh-light: #e6e6e6;
    --swoosh-dark: #6e6e6e;
    --hardware-ribbon: #f5962a;
    --hardware-tip: #d9761a;
    --hardware-panel: #ccdcf5;
    --restore-ribbon: #d83c68;
    --restore-tip: #b22a52;
    --restore-panel: #cfef9c;
    --sash-ribbon: #58c4ef;
    --sash-tip: #d9761a;
    --sash-panel: #efedb4;
  }
  html, body {
    margin: 0;
    padding: 0;
    overflow: hidden;
    background: var(--page);
  }
  .canvas {
    position: relative;
    width: 1200px;
    height: 1200px;
    background: var(--page);
    font-family: "Arimo", Arial, sans-serif;
  }
  .banner {
    position: absolute;
    left: 284px;
    width: 646px;
  }
  .banner-art {
    display: block;
    width: 646px;
    height: 352px;
    outline: 1px solid var(--frame);
  }
  .banner-caption {
    margin: 7px 0 0;
    font-size: 13px;
    line-height: 16px;
    color: var(--caption);
    text-align: center;
    font-weight: 400;
  }
  .banner--hardware { top: 22px; }
  .banner--restore { top: 414px; }
  .banner--sash { top: 812px; }
  .banner--hardware .banner-caption { padding-right: 30px; }
  .banner--sash .banner-caption { padding-left: 40px; }
  .ribbon-text {
    fill: #ffffff;
    font-family: "Arimo", Arial, sans-serif;
    font-weight: 700;
    font-size: 34px;
  }
</style>
</head>
<body>
<main class="canvas">

  <svg width="0" height="0" style="position:absolute" aria-hidden="true">
    <defs>
      <linearGradient id="photo-arched" x1="0" y1="0" x2="1" y2="1">
        <stop offset="0" stop-color="#7d7f7a"/>
        <stop offset="0.5" stop-color="#d9dbd9"/>
        <stop offset="1" stop-color="#8a8a86"/>
      </linearGradient>
      <linearGradient id="photo-casement" x1="0" y1="0" x2="1" y2="1">
        <stop offset="0" stop-color="#f2efe8"/>
        <stop offset="0.55" stop-color="#b9b3a3"/>
        <stop offset="1" stop-color="#4a3b2a"/>
      </linearGradient>
      <linearGradient id="photo-sash" x1="0" y1="0" x2="1" y2="0">
        <stop offset="0" stop-color="#d8d8d0"/>
        <stop offset="0.5" stop-color="#f7f7f5"/>
        <stop offset="1" stop-color="#ffffff"/>
      </linearGradient>
      <linearGradient id="swoosh" x1="0" y1="0" x2="1" y2="0">
        <stop offset="0" stop-color="var(--swoosh-light)"/>
        <stop offset="1" stop-color="var(--swoosh-dark)"/>
      </linearGradient>
      <filter id="text-shadow" x="-10%" y="-20%" width="120%" height="140%">
        <feDropShadow dx="1.5" dy="1.5" stdDeviation="1.2" flood-color="#000" flood-opacity="0.45"/>
      </filter>
      <filter id="ribbon-shadow" x="-10%" y="-10%" width="120%" height="130%">
        <feDropShadow dx="0" dy="3" stdDeviation="4" flood-color="#000" flood-opacity="0.25"/>
      </filter>
    </defs>
  </svg>

  <!-- Hardware -->
  <section class="banner banner--hardware">
    <svg class="banner-art" viewBox="0 0 807 440" xmlns="http://www.w3.org/2000/svg">
      <rect width="807" height="440" fill="#ffffff"/>
      <rect x="342" y="100" width="465" height="340" fill="var(--hardware-panel)"/>
      <path d="M0,0 L240,0 C300,60 275,250 342,440 L0,440 Z" fill="url(#photo-arched)" role="img" aria-label="Photo of an arched black-framed double window looking onto a snowy garden"/>
      <path d="M190,0 C240,5 270,60 285,110" fill="none" stroke="url(#swoosh)" stroke-width="16" stroke-linecap="round"/>
      <g filter="url(#ribbon-shadow)">
        <path d="M335,57 L790,57 L375,373 C330,330 265,290 263,230 C262,195 290,170 310,155 C285,140 265,130 258,118 Z" fill="var(--hardware-ribbon)"/>
      </g>
      <path d="M780,57 L790,57 L795,100 L735,100 Z" fill="var(--hardware-tip)"/>
      <g class="ribbon-text" filter="url(#text-shadow)">
        <text x="328" y="117">Available</text>
        <text x="328" y="162">The Best Model</text>
        <text x="328" y="207">Of Windows</text>
        <text x="328" y="252">Hardware</text>
      </g>
    </svg>
    <p class="banner-caption">New window for sale</p>
  </section>

  <!-- Restoration -->
  <section class="banner banner--restore">
    <svg class="banner-art" viewBox="0 0 807 440" xmlns="http://www.w3.org/2000/svg">
      <rect width="807" height="440" fill="#ffffff"/>
      <rect x="342" y="100" width="465" height="340" fill="var(--restore-panel)"/>
      <path d="M0,0 L240,0 C300,60 275,250 342,440 L0,440 Z" fill="url(#photo-casement)" role="img" aria-label="Photo of a restored white casement window with brass fittings and a snowy view"/>
      <path d="M190,0 C240,5 270,60 285,110" fill="none" stroke="url(#swoosh)" stroke-width="16" stroke-linecap="round"/>
      <g filter="url(#ribbon-shadow)">
        <path d="M335,57 L790,57 L375,373 C330,330 265,290 263,230 C262,195 290,170 310,155 C285,140 265,130 258,118 Z" fill="var(--restore-ribbon)"/>
      </g>
      <path d="M780,57 L790,57 L795,100 L735,100 Z" fill="var(--restore-tip)"/>
      <g class="ribbon-text" filter="url(#text-shadow)">
        <text x="328" y="109">We Provide</text>
        <text x="328" y="154">The Service Of</text>
        <text x="328" y="199">Old Windows</text>
        <text x="328" y="244">Restoration</text>
      </g>
    </svg>
    <p class="banner-caption">Old window restoration</p>
  </section>

  <!-- New sashes -->
  <section class="banner banner--sash">
    <svg class="banner-art" viewBox="0 0 807 440" xmlns="http://www.w3.org/2000/svg">
      <rect width="807" height="440" fill="#ffffff"/>
      <rect x="342" y="100" width="465" height="340" fill="var(--sash-panel)"/>
      <path d="M0,0 L240,0 C300,60 275,250 342,440 L0,440 Z" fill="url(#photo-sash)" role="img" aria-label="Photo of a new painted sliding sash window with brass catches"/>
      <path d="M190,0 C240,5 270,60 285,110" fill="none" stroke="url(#swoosh)" stroke-width="16" stroke-linecap="round"/>
      <g filter="url(#ribbon-shadow)">
        <path d="M335,57 L790,57 L375,373 C330,330 265,290 263,230 C262,195 290,170 310,155 C285,140 265,130 258,118 Z" fill="var(--sash-ribbon)"/>
      </g>
      <path d="M780,57 L790,57 L795,100 L735,100 Z" fill="var(--sash-tip)"/>
      <g class="ribbon-text" filter="url(#text-shadow)">
        <text x="328" y="116">We Make</text>
        <text x="328" y="161">New Sashes</text>
        <text x="328" y="206">and New</text>
        <text x="328" y="251">Windows</text>
      </g>
    </svg>
    <p class="banner-caption">Make new sashes and windows</p>
  </section>

</main>
</body>
</html>
```